Presentation & Communication (Guide, Ebook, carroussel vistelle, corvanet et plumora)

Suite à la conception du logo, je souhaite désormais développer une identité visuelle complète ainsi que des supports marketing pour ma page Plumora, ma communication client interne notamment :
- Couverture Plumora + Photo de profil Plumora
- Guides
- E-books
- Et enfin, une charte graphique destinée aux formulaires sous format Microsoft Forms (pour la collecte de sondages et la prospection).
Vous trouverez ci-joint le logo que vous avez créé, ainsi qu’une couverture que j’ai réalisée via Canva. Cependant, lors de l’importation sur Plumora, le logo et les illustrations apparaissent flous.
Rappel important :
La direction artistique et l’identité visuelle doivent être en parfaite cohérence avec le logo et l’activité, à savoir :
un cabinet d’expertise comptable spécialisé pour les chirurgiens-dentistes et les centres dentaires. Je souhaite quelque chose de minimaliste, haut de gamme et moderne (je veux pas des logos de dents et d'instrument grossier et dans tous les sens).
Les couleurs qui ont été utilisées pour le site sont principalement : #0F1121 ; #FFFFFF ; #4A90A4 ; #5FAFB3.
Les supports doivent être téléchargeable sous format pack office de façon à pouvoir les utiliser et rédiger dessus du texte (guides, e-books, image pour post réseaux sociaux). Il faut donc déterminer une police efficace qui correspond à l'image de mon cabinet comptable (Poppins peut être ?)
Ce que j'aimerais :
1) Une visuel de page de couverture Plu mora
2) Un visuel d'image de profil (Icône) de page Plumora / Vistelle de mon logo
3) Un visuel moderne, haut de gamme et élégant au bon format en utilsant en partie les couleurs évoqué dans le brief. Ce visuel doit être adaptée au format Post publication Vistelle et Plumora avec un visuel autour mais avec la possibilité d'écrire du texte sur le support que vous créér (exemple pièce jointe d'un confrère à moi)
4) Un support Guide de façon également à rédiger dessus simplement avec une bonne typographie moderne et professionnelle, sur plusieurs pages à minima sur 10 pages. Je demande un peu la création d'un thème sous format pack office pour simplifier l'utilisation du fichier et le process pour uniquement éditer et importer sur CorvaNet, Plumora et Vistelle sans transformer ou redymensionner ou rogner la qualité du support. (Deux Exemples ci-joint).
5) Créer un Ebook de la même manière avec un fond (un thème) qui représente bien mon cabinet haut de gamme, classe et moderne. (Exemple Ebook ci-joint)
English :
Following the logo design, I now wish to develop a complete visual identity and marketing materials for my Plumora page and internal client communications, including:
- Plumora cover photo + Plumora profile picture
- Guides
- E-books
- And finally, a style guide for Microsoft Forms forms (for survey collection and lead generation).
Attached you will find the logo you created, as well as a cover photo I designed using Canva. However, when uploaded to Plumora, the logo and illustrations appear blurry.
Important reminder:
The art direction and visual identity must be perfectly consistent with the logo and the business activity, namely:
an accounting firm specializing in services for dentists and dental clinics. I want something minimalist, high-end, and modern (I don't want logos of teeth and crude instruments in all directions).
The colors used for the website are primarily: #0F1121; #FFFFFF; #4A90A4; #5FAFB3.
The materials must be downloadable in Microsoft Office format so they can be used and text added to (guides, e-books, images for social media posts). Therefore, an effective font that matches my accounting firm's image needs to be chosen (Poppins, perhaps?).
What I would like:
1) A Plumora cover image
2) A Plumora/Vistelle profile picture (icon) of my logo
3) A modern, high-end, and elegant image in the correct format, partially using the colors mentioned in the brief. This image must be suitable for Vistelle and Plumora posts, with a surrounding image, but with the option to write text on the document you create (example attached from a colleague).
4) A guide template, also easy to write on, with good, modern, and professional typography, spanning at least 10 pages. I would like a template created in Microsoft Office format to simplify file use and the process of simply editing and importing it to CorvaNet, Plumora, and Vistelle without transforming, resizing, or cropping the document. (Two examples attached).
5) Create an ebook in the same style with a background (theme) that accurately represents my high-end, classy, and modern firm. (Example ebook attached)
Chirurgiens dentistes, orthodontistes
Expertise comptable et conseil fiscal

```html
<!DOCTYPE html>
<html lang="fr">
<head>
<meta charset="utf-8">
<title>VELDAN – Supports de communication</title>
<link rel="stylesheet" href="https://fonts.googleapis.com/css2?family=Montserrat:ital,wght@0,300;0,400;0,500;0,600;0,700;1,700&family=Cormorant+Garamond:wght@600&display=swap">
<style>
  :root{
    --page:#ffffff;
    --label:#222222;
    --night:#0f1121;
    --slate:#232640;
    --sand:#e6dccb;
    --gold:#c9a86a;
    --gold-soft:#b89a62;
    --royal:#0f2c5e;
    --sky:#3d97e0;
    --ink:#ffffff;
  }
  *{box-sizing:border-box;margin:0;padding:0}
  html,body{width:1200px;height:1200px;overflow:hidden;background:var(--page)}
  body{position:relative;font-family:"Montserrat",sans-serif;color:var(--ink)}
  .board-label{position:absolute;color:var(--label);font-weight:400;font-size:17px;letter-spacing:1px;transform:translateX(-50%);white-space:nowrap}

  /* ---------- cover ---------- */
  .cover{position:absolute;left:53px;top:48px;width:810px;height:300px;overflow:hidden;
    background:radial-gradient(ellipse at 60% 40%,#2a2e4a 0%,#1c1f36 55%,#14172a 100%)}
  .cover-lines{position:absolute;inset:0}
  .cover-visual{position:absolute;left:0;top:55px;width:330px;height:245px;
    background:radial-gradient(ellipse at 50% 55%,#6d6a66 0%,#3c3e52 45%,rgba(36,39,62,0) 75%)}
  .cover-brand{position:absolute;left:300px;top:12px;width:210px;text-align:center}
  .mark-ring{display:block;margin:0 auto;width:76px;height:76px;border-radius:50%;border:6px solid var(--sand)}
  .cover-brand .brand-name{font-weight:400;font-size:46px;letter-spacing:3px;color:var(--sand);line-height:1;margin-top:12px}
  .cover-brand .brand-tag{font-size:10px;letter-spacing:.8px;color:#cfc8bb;margin-top:4px;white-space:nowrap}
  .cover-divider{width:145px;height:1px;background:rgba(230,220,203,.45);margin:14px auto 0}
  .cover-text{position:absolute;left:520px;top:100px;width:260px;text-align:center;font-family:"Cormorant Garamond",serif;color:#e9e3d6}
  .cover-text p{font-size:20px;line-height:27px}
  .cover-text .lead{font-size:18.5px}
  .cover-services{font-family:"Montserrat",sans-serif;font-size:13.5px;color:#ddd6c8;margin-top:19px;letter-spacing:.3px}
  .cover-cta{display:inline-block;margin-top:12px;padding:5px 16px;border-radius:14px;background:var(--sand);color:var(--night);font-family:"Montserrat",sans-serif;font-weight:500;font-size:13px}

  /* ---------- profile ---------- */
  .profile{position:absolute;left:936px;top:99px;width:212px;height:212px;border-radius:50%;border:2px solid var(--night);background:#fff}
  .profile-disc{position:absolute;left:7px;top:7px;width:194px;height:194px;border-radius:50%;background:var(--night);text-align:center;padding-top:46px}
  .profile-disc .mark-ring{width:52px;height:52px;border-width:4px}
  .profile-disc .brand-name{font-size:31px;letter-spacing:2px;color:var(--sand);line-height:1;margin-top:10px}
  .profile-disc .brand-tag{font-size:6.6px;color:#e6e1d6;margin-top:3px;letter-spacing:.3px}

  /* ---------- flyer ---------- */
  .flyer{position:absolute;left:53px;top:383px;width:480px;height:720px;overflow:hidden;
    background:linear-gradient(180deg,var(--royal) 0%,#0e2d63 45%,#0b2757 100%)}
  .flyer-shapes{position:absolute;inset:0}
  .flyer-logo{position:absolute;left:40px;top:43px;display:flex;align-items:center;gap:8px;z-index:1}
  .flyer-logo .mark-ring{width:62px;height:62px;border-width:5px;margin:0}
  .flyer-logo .brand-name{font-size:33px;font-weight:400;letter-spacing:1px;color:var(--sand);line-height:1}
  .flyer-logo .brand-tag{font-size:7.4px;color:#e6e1d6;margin-top:5px;letter-spacing:.1px;white-space:nowrap}
  .flyer-title{position:absolute;left:38px;top:198px;font-weight:700;font-size:30px;line-height:35px;letter-spacing:-.3px}
  .flyer-title .accent{color:var(--sky)}
  .flyer-list{position:absolute;left:38px;top:358px;list-style:none;width:400px}
  .flyer-list li{position:relative;padding-left:31px;font-size:17px;line-height:23px;margin-bottom:15px;color:#f1f4fa}
  .flyer-list li b{font-weight:700}
  .flyer-list svg{position:absolute;left:0;top:2px}
  .flyer-tooth{position:absolute;left:404px;top:428px;width:66px;height:92px;border-radius:40% 40% 30% 30%;
    background:radial-gradient(circle at 40% 35%,#ffffff 0%,#dfe8f4 55%,rgba(160,190,230,.3) 100%)}
  .flyer-cta{position:absolute;left:0;width:100%;top:593px;text-align:center;font-size:22px;color:#c9def6}
  .flyer-cta b{color:#fff;font-style:italic;font-weight:700}
  .flyer-contact{position:absolute;left:83px;top:642px;list-style:none;font-size:20px;color:#d8e6f6}
  .flyer-contact li{display:flex;align-items:center;gap:13px;height:31px}

  /* ---------- ebook ---------- */
  .ebook{position:absolute;left:571px;top:472px;width:365px;height:542px;overflow:hidden;
    background:linear-gradient(160deg,#2a2d47 0%,#20233b 60%,#1b1e33 100%)}
  .ebook-art{position:absolute;inset:0}
  .ebook-logo{position:absolute;left:22px;top:21px;display:flex;align-items:center;gap:8px}
  .ebook-logo .mark-ring{width:53px;height:53px;border-width:4px;margin:0}
  .ebook-logo .brand-name{font-size:29px;letter-spacing:1.5px;color:var(--sand);line-height:1}
  .ebook-logo .brand-tag{font-size:8.4px;color:#e6e1d6;margin-top:3px;letter-spacing:.3px;white-space:nowrap}
  .ebook-title{position:absolute;left:26px;top:150px;font-weight:500;font-size:24px;line-height:27.5px;letter-spacing:.6px;color:#f2efe8}
  .ebook-title .small{font-size:19px}
  .ebook-rule{position:absolute;left:20px;top:270px;width:175px;height:1px;background:var(--gold-soft)}
  .ebook-sub{position:absolute;left:26px;top:280px;font-size:12.5px;line-height:18px;letter-spacing:.6px;color:#e0c88e}
  .ebook-badge{position:absolute;left:234px;top:250px;width:124px;height:124px;border-radius:50%;border:3px solid var(--gold);
    background:#20233b;text-align:center;padding-top:20px;font-size:9.8px;line-height:14.6px;letter-spacing:.5px;color:#ede6d6}
  .ebook-footer{position:absolute;left:0;bottom:0;width:100%;height:40px;background:#1f2238;display:flex;align-items:center;justify-content:center;
    font-size:8.6px;letter-spacing:.4px;color:#e6e1d6}
</style>
</head>
<body>

<div class="board-label" style="left:457px;top:12px">Plumora cover</div>

<section class="cover" aria-label="Couverture Plumora">
  <svg class="cover-lines" width="810" height="300" viewBox="0 0 810 300" aria-hidden="true">
    <g fill="none" stroke="#c9a86a" stroke-width="1" opacity=".8">
      <path d="M600 0 L650 30 L810 30"/>
      <path d="M560 0 L620 40 L740 0"/>
      <path d="M810 160 L770 200 L770 245 L690 300"/>
      <path d="M810 210 L720 300"/>
    </g>
    <g fill="none" stroke="#3a3e5c" stroke-width="1">
      <path d="M0 60 L200 160 L370 300"/>
      <path d="M60 0 L260 120"/>
    </g>
    <g fill="#c9a86a" opacity=".85">
      <rect x="452" y="208" width="4" height="8"/><rect x="460" y="200" width="4" height="16"/>
      <rect x="468" y="194" width="4" height="22"/><rect x="476" y="186" width="4" height="30"/>
    </g>
    <path d="M450 200 L470 188 L482 194 L500 178" fill="none" stroke="#c9a86a" stroke-width="1.2"/>
  </svg>
  <div class="cover-visual" role="img" aria-label="Mise en scène : stéthoscope, calculatrice, dent et documents comptables sur un socle"></div>
  <div class="cover-brand">
    <span class="mark-ring"></span>
    <div class="brand-name">VELDAN</div>
    <div class="brand-tag">EXPERTISE COMPTABLE &amp; CONSEIL</div>
    <div class="cover-divider"></div>
  </div>
  <div class="cover-text">
    <p class="lead">Cabinet Comptable Spécialisé</p>
    <p>Chirurgiens-Dentistes</p>
    <p>&amp; Centres Dentaires</p>
    <div class="cover-services">Fiscalité · Gestion · Conseil</div>
    <span class="cover-cta">Contactez-nous</span>
  </div>
</section>

<section class="profile" aria-label="Photo de profil Plumora">
  <div class="profile-disc">
    <span class="mark-ring"></span>
    <div class="brand-name">VELDAN</div>
    <div class="brand-tag">EXPERTISE COMPTABLE ET CONSEIL</div>
  </div>
</section>
<div class="board-label" style="left:1038px;top:344px">Plumora profile picture</div>

<section class="flyer" aria-label="Visuel publication Plumora">
  <svg class="flyer-shapes" width="480" height="720" viewBox="0 0 480 720" aria-hidden="true">
    <defs>
      <linearGradient id="flyerPhoto" x1="0" y1="0" x2="1" y2="1">
        <stop offset="0" stop-color="#dbe6f1"/><stop offset=".6" stop-color="#b9cde2"/><stop offset="1" stop-color="#8fb0d2"/>
      </linearGradient>
    </defs>
    <path d="M0 188 Q120 120 300 150 Q420 170 480 230 L480 720 L0 720 Z" fill="#123876" opacity=".55"/>
    <path d="M0 560 Q180 580 320 520 Q420 480 480 440 L480 720 L0 720 Z" fill="#0c2a5b" opacity=".7"/>
    <path d="M298 0 L480 0 L480 285 Q340 280 292 180 Q262 95 298 0 Z" fill="#3b82d0"/>
    <path role="img" aria-label="Photo : dentiste souriant en blouse blanche dans son cabinet, tenant un modèle dentaire" d="M304 0 L480 0 L480 275 Q348 270 300 180 Q272 95 304 0 Z" fill="url(#flyerPhoto)"/>
    <g fill="#3b74c0" opacity=".35">
      <circle cx="450" cy="300" r="2.5"/><circle cx="465" cy="318" r="2.5"/><circle cx="435" cy="330" r="2.5"/>
      <circle cx="452" cy="345" r="2.5"/><circle cx="468" cy="360" r="2.5"/><circle cx="440" cy="372" r="2.5"/>
      <circle cx="20" cy="650" r="4"/><circle cx="40" cy="668" r="4"/><circle cx="20" cy="690" r="4"/><circle cx="60" cy="690" r="4"/><circle cx="40" cy="708" r="4"/>
    </g>
  </svg>
  <div class="flyer-logo">
    <span class="mark-ring"></span>
    <div>
      <div class="brand-name">VELDAN</div>
      <div class="brand-tag">EXPERTISE COMPTABLE ET CONSEIL</div>
    </div>
  </div>
  <h1 class="flyer-title">Solutions Comptables<br>Pour <span class="accent">Chirurgiens-<br>Dentistes et Centres<br>Dentaires</span></h1>
  <ul class="flyer-list">
    <li><svg width="21" height="21" viewBox="0 0 21 21"><rect width="21" height="21" rx="3" fill="#3d97e0"/><path d="M5 11 L9 15 L16 6" fill="none" stroke="#fff" stroke-width="2.6"/></svg>Gestion optimisée de <b>votre comptabilité</b></li>
    <li><svg width="21" height="21" viewBox="0 0 21 21"><rect width="21" height="21" rx="3" fill="#3d97e0"/><path d="M5 11 L9 15 L16 6" fill="none" stroke="#fff" stroke-width="2.6"/></svg>Accompagnement pour la <b>fiscalitè specifqué</b> aux professions dentaires.</li>
    <li><svg width="21" height="21" viewBox="0 0 21 21"><rect width="21" height="21" rx="3" fill="#3d97e0"/><path d="M5 11 L9 15 L16 6" fill="none" stroke="#fff" stroke-width="2.6"/></svg>Optimisation de la <b>gestion financière</b></li>
    <li><svg width="21" height="21" viewBox="0 0 21 21"><rect width="21" height="21" rx="3" fill="#3d97e0"/><path d="M5 11 L9 15 L16 6" fill="none" stroke="#fff" stroke-width="2.6"/></svg>Conseils personnalisés pour<br>votre cabinet ou centre</li>
  </ul>
  <div class="flyer-tooth" role="img" aria-label="Illustration d'une dent blanche"></div>
  <p class="flyer-cta"><b>Contactez-nous</b> dès aujourd'hui!</p>
  <ul class="flyer-contact">
    <li><svg width="22" height="22" viewBox="0 0 22 22"><rect width="22" height="22" rx="3" fill="#3d97e0"/><path d="M5 6 L17 16 M17 6 L5 16" stroke="#fff" stroke-width="1.6"/></svg>contact@veldan-conseil.com</li>
    <li><svg width="22" height="22" viewBox="0 0 22 22"><rect width="22" height="22" rx="3" fill="#3d97e0"/><path d="M7 5 C5 7 6 11 9 14 C12 17 15 17 17 15 L15 12.5 L13 13.5 C11.5 12.8 9.5 10.8 8.6 9 L9.5 7 Z" fill="#fff"/></svg>01 98 76 54 32</li>
  </ul>
</section>
<div class="board-label" style="left:284px;top:1140px">Plumora flyer</div>

<section class="ebook" aria-label="Couverture e-book">
  <svg class="ebook-art" width="365" height="542" viewBox="0 0 365 542" aria-hidden="true">
    <defs>
      <linearGradient id="ebookPhoto" x1="0" y1="0" x2="1" y2="1">
        <stop offset="0" stop-color="#c9d3de"/><stop offset=".55" stop-color="#9fb3c9"/><stop offset="1" stop-color="#6f8bb0"/>
      </linearGradient>
    </defs>
    <path role="img" aria-label="Photo : dentiste souriant en tenue bleue au cabinet" d="M168 110 Q220 70 365 60 L365 250 Q310 250 280 215 Q220 150 168 110 Z" fill="url(#ebookPhoto)"/>
    <path role="img" aria-label="Photo : équipe dentaire soignant un patient au fauteuil" d="M0 366 C120 364 175 334 215 304 C245 282 275 266 300 262 L365 262 L365 502 Q320 480 250 505 L0 502 Z" fill="url(#ebookPhoto)"/>
    <path d="M0 106 Q120 126 230 88 Q300 62 365 56" fill="none" stroke="#c9a86a" stroke-width="3"/>
    <path d="M160 110 Q230 150 280 215 Q310 250 365 252" fill="none" stroke="#c9a86a" stroke-width="2.5"/>
    <path d="M0 362 C120 360 175 330 215 300 C245 278 275 262 300 258" fill="none" stroke="#c9a86a" stroke-width="2.5"/>
    <path d="M210 505 Q290 480 365 495" fill="none" stroke="#c9a86a" stroke-width="2"/>
  </svg>
  <div class="ebook-logo">
    <span class="mark-ring"></span>
    <div>
      <div class="brand-name">VELDAN</div>
      <div class="brand-tag">EXPERTISE COMPTABLE ET CONSEIL</div>
    </div>
  </div>
  <h2 class="ebook-title">DENTAL<br>SURGEONS<br><span class="small">AND</span> DENTAL<br>CENTERS</h2>
  <div class="ebook-rule"></div>
  <p class="ebook-sub">E-BOOK FOR<br>ACCOUNTING &amp;<br>MANAGEMENT</p>
  <div class="ebook-badge">ESSENTIAL<br>FINANCIAL TIPS<br>&amp; STRATEGIES<br>FOR DENTAL<br>PROFESSIONALS<br>
    <svg width="20" height="12" viewBox="0 0 20 12"><path d="M2 4 L9 10 L18 1" fill="none" stroke="#ede6d6" stroke-width="1.6"/></svg></div>
  <div class="ebook-footer">FINANCIAL TIPS, TAX OPTIMIZATION, PROFITABILITY STRATEGIES</div>
</section>
<div class="board-label" style="left:758px;top:1049px">E-books</div>

</body>
</html>
```